Marketing Flyer for Plumber Referals

8.5" x11" Layout should be landscape not portrait. Create a bold, eye-catching flyer that highlights earning potential from referrals for water damage restoration. Use high-contrast colors like blue, yellow, and white, with bold fonts and dynamic layouts. Include images of restoration work, cash, and happy clients. Emphasize key benefits like $500 minimum payouts, fast payments, and unlimited income potential. Keep instructions simple: refer a client, we handle the work, you get paid. Add a clear call-to-action and display contact details prominently. Focus on professionalism and energy.

Target Market(s)

Plumbers and Contractor 8.5" x11" Layout should be landscape not portrait.

Industry/Entity Type

General Contractor

Colors
0054AA
0677BA
7BADD7
CADEEF
E8F1F8
EB3D1F
EC4F4E
F09395
F8D3D4
FCEDEE

Requirements
Must have
• 8.5" x11" Layout should be landscape not portrait.
Nice to have

```html
<!DOCTYPE html>
<html lang="en">
<head>
<meta charset="utf-8">
<title>Get Paid to Refer a Flood – Referral Flyer</title>
<link href="https://fonts.googleapis.com/css2?family=Cinzel:wght@500;600;700&family=Roboto:wght@400;500;700&display=swap" rel="stylesheet">
<style>
  :root {
    --blue-deep: #1a4f9c;
    --blue: #0054AA;
    --blue-mid: #0677BA;
    --blue-pale: #c5dbeb;
    --red: #e33a2c;
    --red-soft: #EC4F4E;
    --ink: #2b2b2b;
    --body: #444444;
    --white: #ffffff;
    --stage: #5e5e5e;
  }
  * { margin: 0; padding: 0; box-sizing: border-box; }
  html, body { width: 807px; height: 1200px; overflow: hidden; }
  body {
    background: radial-gradient(ellipse at 50% 45%, #6a6a6a 0%, var(--stage) 60%, #555 100%);
    font-family: "Roboto", Arial, sans-serif;
    position: relative;
  }
  .flyer {
    position: absolute;
    left: 76px;
    width: 655px;
    height: 506px;
    overflow: hidden;
    box-shadow: 0 10px 24px rgba(0,0,0,0.45);
  }
  .flyer--front { top: 78px; background: var(--white); }
  .flyer--back { top: 616px; background: var(--blue-pale); }

  /* front */
  .masthead {
    position: absolute; left: 0; top: 0; width: 655px; height: 132px;
    background: var(--blue-deep);
  }
  .masthead__headline {
    position: absolute; left: 36px; top: 30px;
    font-family: "Cinzel", Georgia, serif; font-weight: 600;
    color: var(--white); font-size: 31.5px; letter-spacing: 0.3px; line-height: 1; white-space: nowrap;
  }
  .masthead__subline {
    position: absolute; left: 35px; top: 77px;
    font-family: "Cinzel", Georgia, serif; font-weight: 600;
    color: var(--white); font-size: 25px; letter-spacing: 0.3px; line-height: 1; white-space: nowrap;
  }
  .brand {
    position: absolute; left: 459px; top: 88px; width: 185px;
    font-family: "Roboto", Arial, sans-serif; font-weight: 500;
    color: var(--white); font-size: 13px; letter-spacing: 0.6px; white-space: nowrap;
  }

  .offer-band {
    position: absolute; left: 0; top: 132px; width: 655px; height: 56px;
    background: var(--red);
    display: flex; align-items: center; justify-content: center;
    font-family: "Cinzel", Georgia, serif; font-weight: 600;
    color: var(--white); font-variant: small-caps; letter-spacing: 0.3px;
  }
  .offer-band span { font-size: 32px; white-space: nowrap; }

  .hero-photo {
    position: absolute; left: 430px; top: 188px; width: 225px; height: 273px;
    background:
      radial-gradient(ellipse at 62% 55%, #f4f4f4 0%, #d9d9d9 35%, #9a9a9a 80%, #8a8a8a 100%);
    -webkit-mask-image: linear-gradient(90deg, transparent 0%, #000 35%);
            mask-image: linear-gradient(90deg, transparent 0%, #000 35%);
  }

  .intro {
    position: absolute; left: 36px; top: 213px;
    font-size: 22px; color: var(--ink); font-weight: 400; white-space: nowrap;
  }
  .benefits-title {
    position: absolute; left: 37px; top: 254px;
    font-size: 24px; font-weight: 700; color: var(--ink);
  }
  .benefit { position: absolute; width: 200px; }
  .benefit__icon { position: absolute; left: 0; top: 0; width: 39px; height: 41px; }
  .benefit__title {
    position: absolute; left: 49px; top: -3px; white-space: nowrap;
    font-size: 13.5px; font-weight: 500; color: var(--blue);
  }
  .benefit__text {
    position: absolute; left: 49px; top: 22px; width: 135px;
    font-size: 11.8px; line-height: 17.5px; color: var(--body);
  }
  .benefit--payout { left: 36px; top: 311px; }
  .benefit--leaders { left: 254px; top: 311px; }
  .benefit--evaluation { left: 36px; top: 398px; }
  .benefit--affordable { left: 254px; top: 398px; }
  .benefit--evaluation .benefit__text { text-align: justify; }

  .slogan-bar { position: absolute; left: 0; top: 461px; width: 655px; height: 45px; }
  .slogan-bar__text {
    position: absolute; left: 264px; top: 12px;
    font-size: 17px; font-weight: 700; color: var(--white); white-space: nowrap;
  }

  /* back */
  .back-title {
    position: absolute; left: 0; top: 22px; width: 655px; text-align: center;
    font-family: "Cinzel", Georgia, serif; font-weight: 600;
    font-size: 34px; color: var(--ink); letter-spacing: 0.5px; white-space: nowrap;
  }
  .back-rule {
    position: absolute; left: 86px; top: 70px; width: 483px; height: 2px; background: var(--red-soft);
  }
  .how-title {
    position: absolute; left: 0; top: 91px; width: 655px; text-align: center;
    font-size: 24px; font-weight: 700; color: var(--ink);
  }
  .step { position: absolute; top: 142px; width: 190px; }
  .step--one { left: 29px; }
  .step--two { left: 253px; }
  .step--three { left: 475px; width: 152px; }
  .step__number {
    width: 37px; height: 38px;
    clip-path: polygon(0 8%, 100% 0, 100% 100%, 0 100%);
    display: flex; align-items: center; justify-content: center; padding-top: 3px;
    color: var(--white); font-weight: 700; font-size: 17px;
    background: var(--blue);
  }
  .step--two .step__number { background: var(--red-soft); }
  .step__title {
    margin-top: 17px; font-size: 13.5px; line-height: 17.5px; font-weight: 500; color: var(--blue);
  }
  .step__text { margin-top: 5px; font-size: 11.8px; line-height: 17.5px; color: var(--body); }
  .step--two .step__text, .step--three .step__text { text-align: justify; }

  .cta-bar { position: absolute; left: 0; top: 294px; width: 381px; height: 45px; z-index: 2; }
  .cta-bar__text {
    position: absolute; left: 0; top: 8px; width: 381px; text-align: center;
    font-size: 25px; font-weight: 700; color: var(--white); white-space: nowrap;
  }
  .skyline-photo {
    position: absolute; left: 0; top: 339px; width: 655px; height: 167px;
    background:
      linear-gradient(180deg, #d7cfe0 0%, #c9b3cc 28%, #a77f8e 52%, #7c5c68 68%, #4b3d5a 80%, #3d3d68 100%);
  }
  .contact { position: absolute; left: 402px; z-index: 3; display: flex; align-items: center; gap: 12px; }
  .contact--phone { top: 305px; }
  .contact--web { top: 337px; }
  .contact__icon { width: 23px; height: 23px; flex: none; }
  .contact__text { font-size: 18px; font-weight: 700; color: var(--ink); white-space: nowrap; }
</style>
</head>
<body>

<section class="flyer flyer--front">
  <header class="masthead">
    <h1 class="masthead__headline">EARN UNLIMITED CASH</h1>
    <p class="masthead__subline">GET PAID TO REFER A FLOOD</p>
    <div class="brand">HARBORLINE RESTORATION</div>
  </header>

  <div class="offer-band"><span>$500 Minimum or 10% Per Referral!</span></div>

  <div class="hero-photo" role="img" aria-label="Photo of a white drain pipe leaking splashing water"></div>

  <p class="intro">Partner with the #1 Water Damage Restoration Team</p>
  <h2 class="benefits-title">Why Partner with Us?</h2>

  <div class="benefit benefit--payout">
    <svg class="benefit__icon" viewBox="0 0 39 41"><polygon points="1,5 38,1 38,40 1,40" fill="none" stroke="#0054AA" stroke-width="1.5"/><circle cx="19.5" cy="22" r="7" fill="none" stroke="#e33a2c" stroke-width="1.3" stroke-dasharray="3 1.5"/><circle cx="19.5" cy="22" r="9.5" fill="none" stroke="#e33a2c" stroke-width="1"/></svg>
    <div class="benefit__title">Guaranteed Payout</div>
    <p class="benefit__text">Minimum $500 or 10% of the invoice, paid fast</p>
  </div>

  <div class="benefit benefit--leaders">
    <svg class="benefit__icon" viewBox="0 0 39 41"><polygon points="1,5 38,1 38,40 1,40" fill="none" stroke="#0054AA" stroke-width="1.5"/><g fill="none" stroke="#e33a2c" stroke-width="1.3"><circle cx="19.5" cy="15" r="3.5"/><circle cx="12" cy="18" r="2.8"/><circle cx="27" cy="18" r="2.8"/><path d="M13 29c0-5 3-8 6.5-8s6.5 3 6.5 8z"/><path d="M7 28c0-4 2-6 5-6M32 28c0-4-2-6-5-6"/></g></svg>
    <div class="benefit__title">Industry Leaders</div>
    <p class="benefit__text">Certified experts with 24/7 rapid response.</p>
  </div>

  <div class="benefit benefit--evaluation">
    <svg class="benefit__icon" viewBox="0 0 39 41"><polygon points="1,5 38,1 38,40 1,40" fill="none" stroke="#0054AA" stroke-width="1.5"/><g fill="none" stroke="#e33a2c" stroke-width="1.3"><path d="M12 31l2-6 12-12 4 4-12 12z"/><path d="M23 16l4 4"/></g></svg>
    <div class="benefit__title">Free Evaluations</div>
    <p class="benefit__text">We assess damage and process insurance claims for your clients.</p>
  </div>

  <div class="benefit benefit--affordable">
    <svg class="benefit__icon" viewBox="0 0 39 41"><polygon points="1,5 38,1 38,40 1,40" fill="none" stroke="#0054AA" stroke-width="1.5"/><g fill="none" stroke="#e33a2c" stroke-width="1.3"><rect x="10" y="13" width="19" height="14" rx="1"/><rect x="13" y="16" width="13" height="8"/><path d="M17 27v3h5v-3M14 31h11"/></g></svg>
    <div class="benefit__title">Affordable Solutions</div>
    <p class="benefit__text">Lowest out-of-pocket<br>costs for your customers.</p>
  </div>

  <div class="slogan-bar">
    <svg width="655" height="45" viewBox="0 0 655 45"><polygon points="241,0 655,0 655,45 210,45" fill="#1a4f9c"/></svg>
    <span class="slogan-bar__text">Send Referrals. Get Paid. Grow Your Business</span>
  </div>
</section>

<section class="flyer flyer--back">
  <h2 class="back-title">GET PAID TO REFER A FLOOD</h2>
  <div class="back-rule"></div>
  <h3 class="how-title">How It Works</h3>

  <div class="step step--one">
    <div class="step__number">01</div>
    <div class="step__title">Refer Flood, Water<br>and Mold Damage</div>
    <p class="step__text">Call, book online, or text us directly</p>
  </div>
  <div class="step step--two">
    <div class="step__number">02</div>
    <div class="step__title">We Take Care of<br>Everything</div>
    <p class="step__text">Free evaluations, insurance claims, and professional service.</p>
  </div>
  <div class="step step--three">
    <div class="step__number">03</div>
    <div class="step__title">Get Paid Fast</div>
    <p class="step__text">$500 minimum or 10% of the invoice within 48 hours of final payment.</p>
  </div>

  <div class="skyline-photo" role="img" aria-label="Photo of a city skyline at dusk across the bay"></div>

  <div class="cta-bar">
    <svg width="381" height="45" viewBox="0 0 381 45"><polygon points="31,0 350,0 381,45 0,45" fill="#1a4f9c"/></svg>
    <span class="cta-bar__text">Call Text or Book Online</span>
  </div>

  <div class="contact contact--phone">
    <svg class="contact__icon" viewBox="0 0 23 23"><circle cx="11.5" cy="11.5" r="11.5" fill="#e33a2c"/><path d="M8 6.5l2 2.2-1 1.3c.7 1.6 1.9 2.8 3.5 3.5l1.3-1 2.2 2-1.2 1.8c-3.8-.4-7.6-4.2-8-8z" fill="#fff"/></svg>
    <span class="contact__text">555-014-2738</span>
  </div>
  <div class="contact contact--web">
    <svg class="contact__icon" viewBox="0 0 23 23"><circle cx="11.5" cy="11.5" r="11.5" fill="#1a6fb5"/><rect x="6.5" y="8" width="10" height="7" rx="1" fill="#fff"/><path d="M6.8 8.5l4.7 3.4 4.7-3.4" fill="none" stroke="#1a6fb5" stroke-width="1"/></svg>
    <span class="contact__text">HarborlineRestore.com</span>
  </div>
</section>

</body>
</html>
```